An anniversary gift for my girlfriend

My girlfriend and I have been dating for almost 2 years. We met online and this has afforded us the really unique opportunity to have the first words we said to each other (the whole conversation, in fact) preserved. We're moving in together in a few months and she doesn't know that I saved the conversation. I've been waiting for this to turn it into something we can hang in our new place.

The only phrase I want to use is:
"Well if you dislike people's knees then I think we'll get along famously"

It's an Nobody Leaves Before Midnight in Portland reference for the curious.

I want the poster to use the words themselves as the art; I'm thinking typography. I'd like it to match her aesthetic, she likes to wear Nora Vell and T. Brisk. Colors shouldn't be anything too "girly". Somewhere I'd like to include the date June 1, 2015. It shouldn't be a major piece of the poster though, just a way to denote the date.

It should fit (and be fully visible in) a 16x20 (inches) frame

Thanks in advance for the work!

Requirements
Must have
• Must use only the words: "Well if you dislike people's knees then I think we'll get along famously"
• I want this to be typography, so making the phrase the center of the poster and the art itself.

```html
<!DOCTYPE html>
<html lang="en">
<head>
<meta charset="utf-8">
<title>Well if you dislike people's knees</title>
<link rel="stylesheet" href="https://fonts.googleapis.com/css2?family=Raleway:wght@100;200&family=Montserrat:wght@700&display=swap">
<style>
  :root {
    --gold-light: #f1dca0;
    --gold: #d9b36e;
    --amber: #b87b48;
    --rust: #8a4e3a;
    --umber: #4f2d28;
    --night: #2a2230;
    --cream: #fff6de;
    --blush: #f3b9a6;
    --rose: #d98f86;
    --cocoa: #5a3a30;
    --veil: rgba(255, 246, 225, 0.28);
  }
  html, body {
    margin: 0;
    padding: 0;
    width: 960px;
    height: 1200px;
    overflow: hidden;
    background: var(--night);
  }
  .poster {
    position: relative;
    width: 960px;
    height: 1200px;
    overflow: hidden;
  }
  .backdrop {
    position: absolute;
    inset: 0;
    background:
      radial-gradient(ellipse 60% 35% at 45% 8%, var(--gold-light) 0%, rgba(241,220,160,0) 70%),
      radial-gradient(ellipse 30% 40% at 92% 78%, rgba(232,170,110,0.75) 0%, rgba(232,170,110,0) 70%),
      radial-gradient(ellipse 55% 40% at 45% 55%, var(--rust) 0%, rgba(138,78,58,0) 75%),
      radial-gradient(ellipse 55% 45% at 8% 85%, var(--night) 0%, rgba(42,34,48,0) 75%),
      linear-gradient(180deg, var(--gold) 0%, var(--amber) 35%, var(--rust) 60%, var(--umber) 85%, var(--night) 100%);
  }
  .frame-veil {
    position: absolute;
    inset: 0;
    border: 24px solid var(--veil);
    box-sizing: border-box;
  }
  .frame-line {
    position: absolute;
    inset: 24px;
    border: 1px solid rgba(255, 246, 225, 0.18);
  }
  .quote {
    position: absolute;
    inset: 0;
    margin: 0;
  }
  .quote-line {
    position: absolute;
    left: 0;
    right: 0;
    text-align: center;
    text-transform: uppercase;
    white-space: nowrap;
    line-height: 1;
  }
  .thin {
    font-family: "Raleway", sans-serif;
    font-weight: 100;
    font-size: 104px;
    letter-spacing: 1px;
  }
  .bold {
    font-family: "Montserrat", sans-serif;
    font-weight: 700;
    font-size: 90px;
    letter-spacing: 1px;
    background: linear-gradient(90deg, var(--rose) 0%, var(--blush) 55%, var(--cream) 100%);
    -webkit-background-clip: text;
    background-clip: text;
    color: transparent;
  }
  .line-1 { top: 188px; color: var(--cream); }
  .line-2 { top: 300px; color: var(--cream); }
  .line-3 { top: 415px; color: var(--cream); }
  .line-4 { top: 530px; color: var(--blush); }
  .line-5 { top: 643px; }
  .line-6 { top: 750px; }
  .line-7 { top: 878px; color: rgba(90, 58, 48, 0.8); }
  .date {
    position: absolute;
    right: 30px;
    bottom: 30px;
    font-family: "Raleway", sans-serif;
    font-weight: 200;
    font-size: 19px;
    letter-spacing: 1px;
    color: var(--cocoa);
  }
</style>
</head>
<body>
  <main class="poster">
    <div class="backdrop" role="img" aria-label="Softly blurred warm photograph of sunlit grasses with golden bokeh"></div>
    <div class="frame-veil"></div>
    <div class="frame-line"></div>
    <h1 class="quote">
      <span class="quote-line thin line-1">"Well if you</span>
      <span class="quote-line thin line-2">dislike</span>
      <span class="quote-line thin line-3">people's knees,</span>
      <span class="quote-line thin line-4">then I think</span>
      <span class="quote-line bold line-5">we'll</span>
      <span class="quote-line bold line-6">get along</span>
      <span class="quote-line thin line-7">famously"</span>
    </h1>
    <p class="date">JUNE 1 , 2015</p>
  </main>
</body>
</html>
```